Online Greeting Card Marketplace redesign

PennedNotes.com is a two-sided greeting card marketplace. Buyers purchase hand-made cards online, indicating their message. Sellers hand-write the message and mail directly to recipient.

We are getting decent foot traffic but low sales. I'm also not drawing a lot of Card Designers to sell their products. Feedback has been that it's cluttered, boring, and out of date.

I've always enjoyed vibes such as Lana Brookfield and Delia Hartwell. I was going for pale blues and chocolate browns (as can be seen in PennedNotes Friendbook and Chirpline pages).

Attached document is my not-so-great attempt to redesign, which is uninviting and unpolished.

Need a new homepage and a second similar page when shopping (click on any category to see what I mean, e.g. Halloween).
Updates

Industry/Entity Type

Shopping

Requirements
Must have
• I think my logo (stick drawing of a man with an envelope) is what is currently driving a lot of traffic and should stay in the design, pending minor tweaks.

I'll need all the details of the final design to give to the programmers (font styles, color numbers, etc).

Nice to have
• I was thinking of a dotted frame to surround each picture? White Pearl luminescent or a metallic? I just don't know if it works.

```html
<!DOCTYPE html>
<html lang="en">
<head>
<meta charset="utf-8">
<title>PennedNotes – Hand-made, hand-written, hand-delivered</title>
<link rel="stylesheet" href="https://fonts.googleapis.com/css2?family=Cinzel:wght@400;700&family=PT+Sans:wght@400;700&display=swap">
<style>
:root{
  --sky:#aee4f3;
  --sky-deep:#8fd6ec;
  --brand-blue:#1aa9dc;
  --brand-blue-dark:#0e93c5;
  --title-blue:#1f7fc4;
  --charcoal:#4a4a4a;
  --charcoal-dark:#333;
  --ink:#222;
  --muted:#7a7a7a;
  --panel:#ffffff;
  --caption-bg:rgba(60,60,60,.78);
}
*{box-sizing:border-box;margin:0;padding:0}
html,body{width:1000px;height:1200px;overflow:hidden}
body{
  position:relative;
  font-family:"PT Sans",sans-serif;
  background:radial-gradient(ellipse at 30% 20%,#c6eef9 0%,var(--sky) 45%,var(--sky-deep) 100%);
  color:var(--ink);
}
.abs{position:absolute}
.display{font-family:"Cinzel",serif}

/* header */
.site-header{left:115px;top:23px;width:766px;height:144px;background:var(--panel);border-radius:4px;box-shadow:0 6px 8px rgba(0,0,0,.12)}
.logo-art{left:14px;top:10px;width:205px;height:117px;background:linear-gradient(135deg,#f4f8fb,#dcecf6);border-radius:4px}
.brand-name{left:235px;top:50px;font-size:22px;line-height:1;color:var(--title-blue);letter-spacing:.5px;white-space:nowrap}
.tagline{left:235px;top:79px;font-size:10px;line-height:1;color:#555;letter-spacing:.5px;white-space:nowrap}
.account-block{width:176px}
.account-block h3{font-family:"Cinzel",serif;font-weight:400;font-size:13px;color:var(--title-blue);border-bottom:1px solid #ccc;padding:0 0 2px 24px;position:relative}
.account-block h3::before{content:"";position:absolute;left:4px;top:0;width:14px;height:14px;border-radius:50%;background:var(--brand-blue)}
.account-links{display:flex;gap:22px;margin-top:5px;font-family:"Cinzel",serif;font-size:10.5px;color:#777;white-space:nowrap}
.account-links span::before{content:"";display:inline-block;width:7px;height:8px;background:#999;margin-right:6px;vertical-align:-1px;border-radius:1px}
.account-links.customers{gap:13px}

/* nav */
.main-nav{left:119px;top:183px;width:761px;height:47px;background:var(--brand-blue);display:flex;align-items:center;font-family:"Cinzel",serif;font-size:12.5px;color:#fff;letter-spacing:.4px;white-space:nowrap}
.main-nav .item{height:100%;display:flex;align-items:center;justify-content:center;border-right:1px solid rgba(255,255,255,.25)}
.main-nav .active{width:178px;background:var(--charcoal)}
.search-box{left:577px;top:12px;width:140px;height:20px;background:#fff;border:1px solid #cde;font-family:"PT Sans",sans-serif;font-size:9px;color:#aaa;padding:4px 10px}
.search-go{left:723px;top:12px;width:26px;height:20px;background:var(--charcoal-dark);border:1px solid #fff;font-size:8px;font-weight:700;font-style:italic;font-family:"PT Sans",sans-serif;display:flex;align-items:center;justify-content:center}

/* steps */
.step-tab{top:258px;height:39px;display:flex;align-items:center;justify-content:center;font-family:"Cinzel",serif;font-size:13px;color:#fff;letter-spacing:.4px;white-space:nowrap}
.step-tab.active{background:var(--brand-blue);border:1px solid #fff;border-bottom:none;top:259px;height:40px;padding-top:6px}
.step-tab.idle{background:var(--charcoal)}
.step-panel{left:119px;top:297px;width:761px;height:298px;background:var(--brand-blue);border:1px solid #fff;border-top:none;border-radius:0 0 4px 4px}
.step-inner{left:18px;top:18px;width:730px;height:253px;background:var(--panel)}
.frame{border:3px dotted #111;padding:3px;background:#fff}
.frame .art{width:100%;height:100%}
.feature-card{top:35px;width:182px;height:183px}

/* lower panel */
.content-panel{left:118px;top:630px;width:763px;height:482px;background:var(--panel);border-radius:4px;box-shadow:0 2px 6px rgba(0,0,0,.12)}
.section-title{font-size:20px;color:#555;font-weight:400;letter-spacing:.5px;white-space:nowrap}
.arrow-btn{width:26px;height:26px;border-radius:50%;background:linear-gradient(#fff,#ddd);border:1px solid #bbb}
.arrow-btn svg{display:block}
.side-btn{left:11px;width:125px;height:25px;border-radius:3px;background:var(--brand-blue);color:#fff;font-size:11.5px;display:flex;align-items:center;padding-left:14px;border:1px solid #0c86b7;white-space:nowrap;overflow:hidden}
.side-btn.soft{background:linear-gradient(#6cc6ec,#3aa8da);padding-left:5px;font-size:11px;letter-spacing:-.1px}
.side-btn.soft i{flex:none;width:8px;height:8px;border-radius:50%;background:#fff;margin-right:4px;display:inline-block}
.product{width:135px;height:150px}
.product .inner{position:relative;width:100%;height:100%}
.caption{position:absolute;left:0;right:0;bottom:0;height:35px;background:var(--caption-bg);color:#fff;font-family:"Cinzel",serif;font-size:12px;line-height:13px;padding:4px 12px;letter-spacing:.4px;white-space:nowrap}

/* footer */
.social{top:1135px;width:23px;height:23px;background:#111;border:1px solid #fff}
.footer-links{right:121px;top:1135px;font-size:9px;color:#444;text-align:right;line-height:20px;white-space:nowrap}
</style>
</head>
<body>

<header class="site-header abs">
  <div class="logo-art abs" role="img" aria-label="Hand-drawn stick figure holding up a large blue envelope, standing on a drawn line"></div>
  <div class="brand-name display abs">PENNED NOTES</div>
  <div class="tagline display abs">HAND-MADE. HAND-WRITTEN. HAND-DELIVERED</div>

  <div class="account-block abs" style="left:543px;top:9px">
    <h3>SELLERS</h3>
    <div class="account-links"><span>MY ACCOUNT</span><span>SIGN IN</span></div>
  </div>
  <div class="account-block abs" style="left:543px;top:84px;width:218px">
    <h3 style="width:176px">CUSTOMERS</h3>
    <div class="account-links customers"><span>MY ACCOUNT</span><span>SIGN IN</span><span>CART</span></div>
  </div>
</header>

<nav class="main-nav abs">
  <div class="item active">UPCOMING HOLIDAYS</div>
  <div class="item" style="width:142px">EVERYDAY CARDS</div>
  <div class="item" style="width:113px">BIRTHDAYS</div>
  <div class="item" style="width:140px;border-right:none">ALL CATEGORIES</div>
  <div class="search-box abs">Search</div>
  <div class="search-go abs">GO</div>
</nav>

<div class="step-tab active abs" style="left:119px;width:231px">Step 1 : Choose a Card</div>
<div class="step-tab idle abs" style="left:359px;width:233px">Step 2 : Customize It</div>
<div class="step-tab idle abs" style="left:602px;width:257px">Step 3 : We Handwrite and Mail</div>

<section class="step-panel abs">
  <div class="step-inner abs">
    <div class="feature-card frame abs" style="left:45px"><div class="art" role="img" aria-label="Hand-made birthday card with a green and purple lace rosette" style="background:linear-gradient(135deg,#e8efe9,#c9d9c4 55%,#9a6f9a)"></div></div>
    <div class="feature-card frame abs" style="left:270px"><div class="art" role="img" aria-label="Card shaped like a gold shirt with a red sparkling tie and the number 21" style="background:linear-gradient(135deg,#8c1f2e,#c9a866 50%,#f3ece6)"></div></div>
    <div class="feature-card frame abs" style="left:504px"><div class="art" role="img" aria-label="Party invitation card with a pink paper hippo and a red flower" style="background:linear-gradient(135deg,#f2e6ea,#e86a7f 60%,#d9334e)"></div></div>
  </div>
</section>

<section class="content-panel abs">
  <h2 class="section-title display abs" style="left:155px;top:18px">UPCOMING HOLIDAYS</h2>
  <div class="arrow-btn abs" style="left:662px;top:21px"><svg width="24" height="24"><path d="M14 7 L9 12 L14 17" fill="none" stroke="#222" stroke-width="2.5"/></svg></div>
  <div class="arrow-btn abs" style="left:696px;top:21px"><svg width="24" height="24"><path d="M10 7 L15 12 L10 17" fill="none" stroke="#222" stroke-width="2.5"/></svg></div>

  <div class="side-btn soft abs" style="top:67px"><i></i>Follow Us Friendbook</div>
  <div class="side-btn soft abs" style="top:100px"><i></i>Follow Us Chirpline</div>
  <div class="side-btn abs" style="top:134px">About Us / FAQ</div>
  <div class="side-btn abs" style="top:169px">Contact</div>

  <div class="product frame abs" style="left:154px;top:62px"><div class="inner"><div class="art" role="img" aria-label="Card with a girl holding a pink balloon among flowers" style="background:linear-gradient(135deg,#c84a5a,#e9d8d4 50%,#7db1c4)"></div><div class="caption">Halloween<br>By Creator</div></div></div>
  <div class="product frame abs" style="left:305px;top:62px"><div class="inner"><div class="art" role="img" aria-label="Card with a pink paper bird on a branch" style="background:linear-gradient(135deg,#e6e0d8,#d8456e 60%,#b6d4e6)"></div><div class="caption">Labor<br>By Creator</div></div></div>
  <div class="product frame abs" style="left:456px;top:62px"><div class="inner"><div class="art" role="img" aria-label="Card with pink patterned paper and a lavender rosette" style="background:linear-gradient(135deg,#c9448a,#e8c7d8 55%,#7c4a9c)"></div><div class="caption">Halloween<br>By Creator</div></div></div>
  <div class="product frame abs" style="left:607px;top:62px"><div class="inner"><div class="art" role="img" aria-label="Red card with white paper roses on stems" style="background:linear-gradient(135deg,#e5452a,#f06a4a 60%,#c93a22)"></div><div class="caption">Labor Day<br>By Creator</div></div></div>

  <h2 class="section-title display abs" style="left:155px;top:260px">NEW CARDS</h2>
  <div class="arrow-btn abs" style="left:662px;top:264px"><svg width="24" height="24"><path d="M14 7 L9 12 L14 17" fill="none" stroke="#222" stroke-width="2.5"/></svg></div>
  <div class="arrow-btn abs" style="left:696px;top:264px"><svg width="24" height="24"><path d="M10 7 L15 12 L10 17" fill="none" stroke="#222" stroke-width="2.5"/></svg></div>

  <div class="product frame abs" style="left:154px;top:304px"><div class="inner"><div class="art" role="img" aria-label="Card with a round brown robin beside a blue polka-dot panel" style="background:linear-gradient(135deg,#ece8e4,#8a4a3a 50%,#9cc8e4)"></div><div class="caption">Birthday<br>By Creator</div></div></div>
  <div class="product frame abs" style="left:305px;top:304px"><div class="inner"><div class="art" role="img" aria-label="Card with a glittering gold number 21" style="background:linear-gradient(135deg,#f1ede4,#d6b870 55%,#c0c0c0)"></div><div class="caption">Anniversary<br>By Creator</div></div></div>
  <div class="product frame abs" style="left:456px;top:304px"><div class="inner"><div class="art" role="img" aria-label="Plaid festive card with a champagne glass and a red medallion" style="background:linear-gradient(135deg,#c92a32,#f4ecd8 50%,#2f7a45)"></div><div class="caption">Berevement<br>By Creator</div></div></div>
  <div class="product frame abs" style="left:607px;top:304px"><div class="inner"><div class="art" role="img" aria-label="Card with a girl holding a pink balloon among flowers" style="background:linear-gradient(135deg,#c84a5a,#e9d8d4 50%,#7db1c4)"></div><div class="caption">New Baby<br>By Creator</div></div></div>
</section>

<footer>
  <div class="social abs" style="left:118px"></div>
  <div class="social abs" style="left:151px"></div>
  <div class="social abs" style="left:183px"></div>
  <div class="social abs" style="left:215px"></div>
  <div class="social abs" style="left:247px"></div>
  <div class="footer-links abs">
    Blog &nbsp;|&nbsp; Terms &nbsp;|&nbsp; Privacy Policy &nbsp;|&nbsp; Sitemap<br>
    © 2013 pennednotes, All Rights Reserved<br>
    X2
  </div>
</footer>

</body>
</html>
```